Aerospace Private Equity Firm Needs Website

We need a website for new private equity fund called Orlin Partners. We buy smaller companies in the aerospace and industrial industries. I have attached some information about the firm. An example of a site we like that is a similar business but focused in a different sector is www.travomedic.com. www.quarnestgrove.com is a firm that also invests in aerospace companies.

Industry/Entity Type

Equity

Number of Pages Required

1 page

Colors
0555a3
33a6d7
ec1f27

```html
<!DOCTYPE html>
<html lang="en">
<head>
<meta charset="utf-8">
<title>Orlin Partners</title>
<link href="https://fonts.googleapis.com/css2?family=Raleway:wght@400;500;600;700&family=Arimo:wght@400;700&display=swap" rel="stylesheet">
<style>
:root{
  --navy:#0a3a8f;
  --blue:#0555a3;
  --sky:#33a6d7;
  --red:#ec1f27;
  --ink:#222;
  --grey-bg:#f2f2f2;
  --footer:#151515;
  --footer-deep:#050505;
}
*{margin:0;padding:0;box-sizing:border-box}
html,body{width:698px;height:1200px;overflow:hidden;background:#fff}
body{position:relative;font-family:'Raleway',sans-serif;color:var(--ink)}
.abs{position:absolute}
.topnav{left:0;top:0;width:698px;height:26px;background:var(--navy);display:flex;align-items:center}
.topnav a{position:absolute;color:#fff;font-size:10px;text-decoration:none;top:7px}
.topnav a.active{color:var(--red)}
.masthead{top:26px;left:0;width:698px;height:59px}
.brand{left:55px;top:14px;font-size:26px;font-weight:600;color:var(--blue);display:flex;align-items:center;gap:6px}
.brand i{width:10px;height:10px;background:var(--red);border-radius:50%;display:block}
.phone{top:20px;display:flex;align-items:center;gap:6px}
.phone small{display:block;font-size:7px;color:#222}
.phone b{display:block;font-size:11px;font-weight:500;color:#111}
.hero{top:85px;left:0;width:698px;height:243px;background:radial-gradient(circle at 48% 55%,#c9a25a 0,#4a6b8a 18%,#1e56a8 40%,#0b2e6b 100%)}
.hero-arrow{top:104px;width:20px;height:20px;background:#555;border:1px solid #ccc}
.hero-caption{left:120px;top:187px;width:458px;height:36px;background:rgba(30,50,90,.55);color:#fff;font-size:12px;font-weight:600;text-align:center;line-height:17px;padding-top:2px}
.feature{top:320px;width:190px;text-align:center}
.feature .disc{width:74px;height:74px;border-radius:50%;margin:0 auto;background:#f3f3f3;border:2px solid #fff;box-shadow:0 0 0 1px #ddd,0 5px 6px -3px #ccc;display:flex;align-items:center;justify-content:center}
.feature h3{margin-top:18px;font-size:10.5px;font-weight:600;color:var(--blue)}
.feature p{margin-top:9px;font-family:'Arimo',sans-serif;font-size:7.6px;line-height:12px;color:#222}
.feature a{display:inline-block;margin-top:6px;font-family:'Arimo',sans-serif;font-size:8.5px;color:var(--blue)}
.feature a.red{color:var(--red)}
.why{top:522px;left:0;width:698px;height:248px;background:var(--grey-bg)}
.why-title{right:456px;top:95px;text-align:right;font-size:26px;font-weight:700;color:var(--blue);line-height:40px}
.why-rule{left:253px;top:35px;width:1px;height:178px;background:#bbb}
.why-item{left:271px;width:375px}
.why-item h4{font-size:10.5px;font-weight:600;color:#222}
.why-item p{font-family:'Arimo',sans-serif;font-size:7.4px;line-height:12px;color:#222}
.why-tick{left:252px;width:4px;height:14px;background:var(--red)}
.partners-title{top:796px;left:0;width:698px;text-align:center;font-size:20px;font-weight:600;color:var(--navy)}
.partners-title span{color:var(--red)}
.tile{width:111px;height:46px;border:1px solid #e6e6e6;background:#fff;display:flex;align-items:center;justify-content:center}
.footer{top:988px;left:0;width:698px;height:212px;background:var(--footer)}
.footer-bar{top:1168px;left:0;width:698px;height:32px;background:var(--footer-deep)}
.inquiry{top:988px;left:38px;width:179px;height:212px;background:linear-gradient(#0a4fb5,#063b93)}
.inquiry h2{position:absolute;left:17px;top:24px;font-size:13px;font-weight:500;color:#fff}
.field{position:absolute;left:17px;width:145px;height:17px;background:#3c6fc6;color:#e8eefc;font-size:7.5px;padding:4px 6px}
.submit{position:absolute;left:16px;top:173px;width:40px;height:14px;background:var(--red);color:#fff;font-size:8px;font-weight:700;text-align:center;line-height:14px}
.col-title{top:1020px;font-size:10.5px;color:#fff}
.col-rule{top:1039px;width:40px;height:1px;background:#fff}
.quicklinks{left:250px;top:1052px;font-size:8px;line-height:14.5px;color:#fff}
.quicklinks div:first-child{color:var(--red)}
.contact{left:377px;color:#fff;font-size:8px;line-height:10.5px}
.foot-brand{left:537px;top:1060px;font-size:24px;font-weight:600;color:#e6e6e6;display:flex;align-items:center;gap:6px}
.foot-brand i{width:9px;height:9px;background:#e6e6e6;border-radius:50%;display:block}
.copyright{top:1179px;left:243px;font-size:7.6px;color:#fff}
</style>
</head>
<body>
<nav class="abs topnav">
  <a class="active" style="left:55px">Home</a>
  <a style="left:115px">Overview</a>
  <a style="left:188px">Team</a>
  <a style="left:245px">Investment Strategy</a>
  <a style="left:367px">Investment Performance</a>
  <a style="left:508px">Case Study</a>
  <a style="left:593px">Contact Us</a>
</nav>

<header class="abs masthead">
  <div class="abs brand"><i></i>Orlin Partners</div>
  <div class="abs phone" style="left:432px">
    <svg width="18" height="18" viewBox="0 0 18 18"><circle cx="9" cy="9" r="8" fill="none" stroke="var(--blue)" stroke-width="1.2"/><path d="M6 5q-1 4 3 8l2-1-1-2-1 1q-2-2-2-4l1-1-1-2z" fill="var(--blue)"/></svg>
    <div><small>ORLIN PARTNERS</small><b>(310) 555-0142</b></div>
  </div>
  <div class="abs phone" style="left:540px">
    <svg width="18" height="18" viewBox="0 0 18 18"><circle cx="9" cy="9" r="8" fill="none" stroke="#111" stroke-width="1.2"/><path d="M6 5q-1 4 3 8l2-1-1-2-1 1q-2-2-2-4l1-1-1-2z" fill="#111"/></svg>
    <div><small>TELLAN CAPITAL</small><b>(203) 555-0187</b></div>
  </div>
</header>

<section class="abs hero" role="img" aria-label="Aerospace and industrial montage: jet engine fan, airliner, circuit board and refinery at night">
  <div class="abs hero-arrow" style="left:4px"><svg width="18" height="18"><path d="M11 5l-4 4 4 4" stroke="#fff" stroke-width="2" fill="none"/></svg></div>
  <div class="abs hero-arrow" style="left:670px"><svg width="18" height="18"><path d="M7 5l4 4-4 4" stroke="#fff" stroke-width="2" fill="none"/></svg></div>
  <div class="abs hero-caption">Orlin Focuses on Lower Middle-market Control Investments In Aerospace And Industrial Companies Based In North America.</div>
</section>

<div class="abs feature" style="left:33px">
  <div class="disc"><svg width="34" height="30" viewBox="0 0 34 30"><path d="M2 28V14l7 5v-5l7 5v-5l7 5v9z" fill="var(--blue)"/><path d="M16 12l14-9 2 2-9 11-1-4z" fill="var(--blue)"/></svg></div>
  <h3>Our Investments</h3>
  <p>Deep network of people, companies, resources: Metallic Structures, Fluid Conveyance, Composite Structures &amp; Surface Treatment</p>
  <a class="red">Read More</a>
</div>
<div class="abs feature" style="left:249px">
  <div class="disc"><svg width="32" height="32" viewBox="0 0 32 32"><circle cx="15" cy="17" r="13" fill="none" stroke="var(--blue)" stroke-width="3"/><circle cx="15" cy="17" r="7" fill="none" stroke="var(--blue)" stroke-width="3"/><circle cx="15" cy="17" r="2.5" fill="var(--blue)"/><path d="M15 17L29 3" stroke="var(--blue)" stroke-width="2.5"/></svg></div>
  <h3>Our Strategy</h3>
  <p>Companies that share common characteristics with aerospace: Regulated quality control, Product certification, Precision manufacturing &amp; Engineering driven</p>
  <a>Read More</a>
</div>
<div class="abs feature" style="left:465px">
  <div class="disc"><svg width="40" height="28" viewBox="0 0 40 28"><circle cx="10" cy="8" r="5" fill="var(--blue)"/><circle cx="30" cy="8" r="5" fill="var(--blue)"/><circle cx="20" cy="7" r="6" fill="var(--blue)"/><path d="M1 26q0-12 9-12t9 12zM21 26q0-12 9-12t9 12zM10 27q0-14 10-14t10 14z" fill="var(--blue)"/></svg></div>
  <h3>Our Team</h3>
  <p>Founded in 2016 by Principals from Westbrook Hill Associates (WHA) – Los Angeles, CA. $200 million with hard cap of $250 million</p>
  <a>Read More</a>
</div>

<section class="abs why">
  <div class="abs why-title">WHY<br>CHOOSE US ?</div>
  <div class="abs why-rule"></div>
  <div class="abs why-tick" style="top:45px"></div>
  <div class="abs why-tick" style="top:98px"></div>
  <div class="abs why-tick" style="top:149px"></div>
  <div class="abs why-item" style="top:45px"><h4>Over 50 years Years of Experience</h4><p>Lorem ipsum dolor sit amet, consectetuer adipiscing elit, sed diam nonummy nibh euismod tincidunt ut laoreet dolore magna aliquam erat volutpat.</p></div>
  <div class="abs why-item" style="top:99px"><h4>Fully Trained and Credentialed</h4><p>Lorem ipsum dolor sit amet, consectetuer adipiscing elit, sed diam nonummy nibh euismod tincidunt ut laoreet dolore magna aliquam erat volutpat.</p></div>
  <div class="abs why-item" style="top:150px"><h4>Great Business Knowledge</h4><p>Lorem ipsum dolor sit amet, consectetuer adipiscing elit, sed diam nonummy nibh euismod tincidunt ut laoreet dolore magna aliquam erat volutpat.</p></div>
</section>

<h2 class="abs partners-title">O<span>u</span>r Partners</h2>
<svg class="abs" style="left:340px;top:828px" width="18" height="10"><path d="M1 1l8 8 8-8" stroke="var(--red)" stroke-width="2.5" fill="none"/></svg>

<div class="abs tile" style="left:55px;top:853px"><svg width="30" height="30"><circle cx="15" cy="15" r="12" fill="#1d3f8f"/></svg></div>
<div class="abs tile" style="left:175px;top:853px"><svg width="48" height="30"><rect x="1" y="3" width="46" height="24" fill="var(--red)"/></svg></div>
<div class="abs tile" style="left:294px;top:853px"><svg width="70" height="16"><rect x="1" y="3" width="68" height="10" fill="#8a8a8a"/></svg></div>
<div class="abs tile" style="left:413px;top:853px"><svg width="34" height="34"><circle cx="17" cy="17" r="14" fill="#2c4ea0"/></svg></div>
<div class="abs tile" style="left:532px;top:853px"><svg width="80" height="16"><rect x="1" y="3" width="78" height="10" fill="#1b5db8"/></svg></div>
<div class="abs tile" style="left:55px;top:909px"><svg width="80" height="16"><rect x="1" y="2" width="78" height="12" fill="#8e1a1a"/></svg></div>
<div class="abs tile" style="left:175px;top:909px"><svg width="32" height="30"><rect x="2" y="2" width="28" height="26" fill="#d42020"/></svg></div>
<div class="abs tile" style="left:294px;top:909px"><svg width="80" height="16"><rect x="1" y="3" width="78" height="10" fill="#444"/></svg></div>
<div class="abs tile" style="left:413px;top:909px"><svg width="30" height="30"><rect x="3" y="3" width="24" height="24" fill="#14306e"/></svg></div>
<div class="abs tile" style="left:532px;top:909px"><svg width="80" height="14"><rect x="1" y="3" width="78" height="8" fill="#223f8a"/></svg></div>

<footer class="abs footer"></footer>
<div class="abs footer-bar"></div>
<form class="abs inquiry">
  <h2>Quick Inquiry</h2>
  <div class="field" style="top:48px">Name</div>
  <div class="field" style="top:72px">Phone</div>
  <div class="field" style="top:96px">Email</div>
  <div class="field" style="top:120px;height:47px">Message</div>
  <div class="submit">Submit</div>
</form>

<div class="abs col-title" style="left:250px">Quick links</div>
<div class="abs col-rule" style="left:250px"></div>
<div class="abs quicklinks">
  <div>Home</div><div>Overview</div><div>Team</div><div>Investment Strategy</div><div>Investment Performance</div><div>Case Study</div><div>Contact Us</div>
</div>

<div class="abs col-title" style="left:377px">Contact Details</div>
<div class="abs col-rule" style="left:377px"></div>
<svg class="abs" style="left:377px;top:1055px" width="10" height="14"><path d="M5 13Q0 7 0 5a5 5 0 0110 0q0 2-5 8z" fill="var(--red)"/><circle cx="5" cy="5" r="2" fill="var(--footer)"/></svg>
<div class="abs contact" style="left:396px;top:1055px">2480 Harbor View Blvd.<br>Suite 410<br>Los Angeles, CA 90067</div>
<svg class="abs" style="left:377px;top:1099px" width="12" height="12"><path d="M3 2q-2 5 4 9l2-2-2-2-1 1q-2-1-2-3l1-1-1-2z" fill="none" stroke="var(--red)"/></svg>
<div class="abs contact" style="left:396px;top:1100px">(310) 555-0142</div>
<svg class="abs" style="left:377px;top:1126px" width="13" height="10"><rect x=".5" y=".5" width="12" height="9" fill="none" stroke="var(--red)"/><path d="M1 1l5.5 5L12 1" fill="none" stroke="var(--red)"/></svg>
<div class="abs contact" style="left:398px;top:1126px">inquiry@orlinpartners.com</div>

<div class="abs foot-brand"><i></i>Orlin Partners</div>
<div class="abs copyright">Copyright © 2017 Orlin Partners | Privacy Policy | User Agreement</div>
</body>
</html>
```